Glorvanta Letterhead and Template Design

We are looking to freshen up and modernise our business letter heads and cover pages for our documents. Looking at a suit of new designs. I would like a design for:
- Letter Head
- Page 2 follower (for lengthy documents) - fancy
- Page 2 follower (for lengthy documents) - simple version
- Cover Page for reports to sent to client
- Cover Page for internal documents.

Our website is www.glorvanta.com.au.

I have attached a copy of our current brochure for inspiration and our old letter head so you can see what we currently use.

On our Client Cover Page and letter head we would like to include out business awards. Happy for you to change these designs if you have something that would look better. Have also included logos and awards. We won the Meridian Vermin Control Honour in 2022/23 and also in 2019/2020. We were a state finalist in the Quorvel Enterprise Prizes this year logo attached.

We like the emblem to be watermarked into the page in the background.

We want something fresh/clean/modern and classy.

Letter head needs to include our Phone Number: 1300591037
Email: hello@glorvanta.com.au
Text: 0472913508
Website: www.glorvanta.com.au

```html
<!DOCTYPE html>
<html lang="en">
<head>
<meta charset="utf-8">
<title>Glorvanta Letterhead</title>
<link href="https://fonts.googleapis.com/css2?family=Poppins:wght@400;500;600&display=swap" rel="stylesheet">
<style>
  :root {
    --backdrop: #e9e9e9;
    --paper: #ffffff;
    --paper-shade: #f1f1f0;
    --ink: #3a3a3a;
    --brand-grey: #6b6c6e;
    --brand-green: #7bbf55;
    --watermark: #ecece8;
  }
  * { margin: 0; padding: 0; box-sizing: border-box; }
  html, body {
    width: 1200px;
    height: 1200px;
    overflow: hidden;
    background: var(--backdrop);
    font-family: "Poppins", sans-serif;
  }
  .letterhead {
    position: absolute;
    left: 204px;
    top: 40px;
    width: 792px;
    height: 1120px;
    background: linear-gradient(160deg, var(--paper) 0%, var(--paper-shade) 100%);
    overflow: hidden;
  }
  .brand {
    position: absolute;
    left: 40px;
    top: 34px;
    display: flex;
    align-items: center;
    gap: 12px;
  }
  .brand-dot {
    width: 26px;
    height: 26px;
    border-radius: 50%;
    background: var(--brand-green);
  }
  .brand-name {
    font-weight: 600;
    font-size: 42px;
    line-height: 1;
    color: var(--brand-grey);
    letter-spacing: 0.5px;
  }
  .watermark {
    position: absolute;
    left: 161px;
    top: 297px;
    width: 552px;
    height: 552px;
    border-radius: 50%;
    background: var(--watermark);
    opacity: 0.7;
  }
  .side-web {
    position: absolute;
    left: 40px;
    top: 475px;
    font-size: 14px;
    color: var(--ink);
    writing-mode: vertical-rl;
    transform: rotate(180deg);
    letter-spacing: 0.2px;
  }
  .side-marker {
    position: absolute;
    left: 41px;
    top: 658px;
    width: 11px;
    height: 19px;
    background: var(--brand-green);
  }
  .contact {
    position: absolute;
    left: 40px;
    top: 1028px;
    font-size: 14.5px;
    line-height: 22.5px;
    color: var(--ink);
    list-style: none;
  }
  .contact-label { font-weight: 500; }
</style>
</head>
<body>
  <main class="letterhead">
    <div class="brand">
      <span class="brand-dot"></span>
      <span class="brand-name">Glorvanta</span>
    </div>

    <div class="watermark" role="img" aria-label="Faint brand watermark area"></div>

    <div class="side-web">www.glorvanta.com.au</div>
    <div class="side-marker"></div>

    <ul class="contact">
      <li><span class="contact-label">Phone:</span> 1300591037</li>
      <li><span class="contact-label">Email:</span> hello@glorvanta.com.au</li>
      <li><span class="contact-label">Text:</span> 0472913508</li>
    </ul>
  </main>
</body>
</html>
```